Box Truck Design for a Custom Bedding company in the Marine Industry

We are looking for a creative Modern design for our box truck. I needs to Include our Icon (sailboat, moon and water) and perhaps our full logo with our stylized name of harborslumber.net. It needs to include out phone number" (800) 555-2741 our website written out "www.harborslumber.net" and our service offering of " Custom Boat Mattresses and Bedding" . Our box will be silver. I've included a pdf of the general shape of our box as it's a former Q-move truck so it has a part of the box that over hangs the cab. We want a design that is modern an clean but still catches the eye. In the pdf of the mock up there is a dark silver strip. That is metal trim that will not be wrapped. And the strip of grey below the metal trim has texture so information can not be placed there, however feel free to change the color of that section or or place part of the overall design in that section. I don't need design for the front of the truck or the back. I just need the side artwork, unless you have an idea for the back that looks great with the sides.

Font styles to use
Serif
Sans Serif

Colors
0655a3
ec1f27
ffffff

Requirements
Must have
• The mock up should show the background of the box as silver and the cab of the truck as silver as well.
Nice to have
• We like the look of having our Icon (Sailboat, Moon and Water) really large on the Box and towards the back of the truck.
Should not have
• We do not want to have pictures of beds or our products on the truck.

```html
<!DOCTYPE html>
<html lang="en">
<head>
<meta charset="utf-8">
<title>Harbor Slumber – Box Truck Wrap Panels</title>
<link href="https://fonts.googleapis.com/css2?family=Arimo:wght@400;700&display=swap" rel="stylesheet">
<style>
  :root {
    --blue: #0655a3;
    --red: #ec1f27;
    --white: #ffffff;
    --silver-light: #e4e6e9;
    --silver-dark: #b9bdc3;
    --panel-edge: #8a8d92;
    --page: #ffffff;
  }
  html, body {
    margin: 0;
    padding: 0;
    width: 1200px;
    height: 1200px;
    overflow: hidden;
    background: var(--page);
  }
  .canvas {
    width: 1200px;
    height: 1200px;
    display: flex;
    align-items: center;
    justify-content: center;
  }
  .wrap-panels {
    width: 1170px;
    height: 263px;
    font-family: "Arimo", Arial, sans-serif;
  }
  .band-red { fill: var(--red); }
  .band-blue { fill: var(--blue); }
  .panel-silver { fill: url(#silver); stroke: var(--panel-edge); stroke-width: 1; }
  .phone { fill: var(--white); font-weight: 700; }
  .url { fill: var(--white); font-weight: 400; font-size: 12px; }
  .service-red { fill: var(--red); }
  .service-blue { fill: var(--blue); }
  .bold { font-weight: 700; }
  .regular { font-weight: 400; }
  .brand-mark { fill: var(--blue); }
  .brand-name { fill: var(--blue); font-weight: 700; }
</style>
</head>
<body>
<main class="canvas">
  <svg class="wrap-panels" viewBox="0 0 1405 316" xmlns="http://www.w3.org/2000/svg">
    <defs>
      <linearGradient id="silver" x1="0" y1="0" x2="0" y2="1">
        <stop offset="0" stop-color="var(--silver-light)"/>
        <stop offset="1" stop-color="var(--silver-dark)"/>
      </linearGradient>
    </defs>

    <!-- Driver side panel -->
    <g class="side-left">
      <rect class="panel-silver" x="106" y="0" width="449" height="258"/>
      <rect class="band-red" x="0" y="0" width="555" height="28"/>
      <rect class="band-blue" x="0" y="35" width="400" height="50"/>
      <text class="phone" x="18" y="73" font-size="34">(800) 555-2741</text>
      <polygon class="band-red" points="160,90 328,90 322,108 166,108"/>
      <text class="url" x="244" y="104" text-anchor="middle">www.harborslumber.net</text>
      <text x="300" y="153" text-anchor="end"><tspan class="service-red bold" font-size="26">CUSTOM</tspan><tspan class="service-red regular" font-size="20">BOAT</tspan></text>
      <text x="300" y="174" text-anchor="end"><tspan class="service-red bold" font-size="17">MATTRESSES</tspan><tspan class="service-blue bold" font-size="24">AND</tspan></text>
      <text class="service-blue bold" x="300" y="208" text-anchor="end" font-size="42">BEDDING</text>
      <g class="brand" role="img" aria-label="Harbor Slumber brand name">
        <circle class="brand-mark" cx="440" cy="100" r="62"/>
        <text class="brand-name" x="440" y="205" text-anchor="middle" font-size="22">Harbor Slumber</text>
      </g>
    </g>

    <!-- Rear door panel -->
    <g class="rear">
      <rect class="panel-silver" x="555" y="0" width="295" height="316"/>
      <text x="835" y="31" text-anchor="end"><tspan class="service-red bold" font-size="26">CUSTOM</tspan><tspan class="service-red regular" font-size="20">BOAT</tspan></text>
      <text x="835" y="58" text-anchor="end"><tspan class="service-red bold" font-size="17">MATTRESSES</tspan><tspan class="service-blue bold" font-size="24">AND</tspan></text>
      <text class="service-blue bold" x="835" y="93" text-anchor="end" font-size="42">BEDDING</text>
      <g class="brand" role="img" aria-label="Harbor Slumber brand name">
        <circle class="brand-mark" cx="702" cy="158" r="40"/>
        <text class="brand-name" x="702" y="222" text-anchor="middle" font-size="16">Harbor Slumber</text>
      </g>
      <rect class="band-red" x="556" y="256" width="293" height="17"/>
      <text class="url" x="702" y="269" text-anchor="middle">www.harborslumber.net</text>
      <rect class="band-blue" x="556" y="275" width="293" height="35"/>
      <text class="phone" x="702" y="303" text-anchor="middle" font-size="26">(800) 555-2741</text>
    </g>

    <!-- Curb side panel -->
    <g class="side-right">
      <rect class="panel-silver" x="850" y="0" width="448" height="258"/>
      <rect class="band-red" x="850" y="0" width="555" height="28"/>
      <rect class="band-blue" x="1080" y="35" width="325" height="50"/>
      <text class="phone" x="1385" y="73" text-anchor="end" font-size="34">(800) 555-2741</text>
      <polygon class="band-red" points="1120,90 1278,90 1272,108 1126,108"/>
      <text class="url" x="1199" y="104" text-anchor="middle">www.harborslumber.net</text>
      <g class="brand" role="img" aria-label="Harbor Slumber brand name">
        <circle class="brand-mark" cx="988" cy="100" r="62"/>
        <text class="brand-name" x="988" y="205" text-anchor="middle" font-size="22">Harbor Slumber</text>
      </g>
      <text x="1288" y="186" text-anchor="end"><tspan class="service-red bold" font-size="26">CUSTOM</tspan><tspan class="service-red regular" font-size="20">BOAT</tspan></text>
      <text x="1288" y="209" text-anchor="end"><tspan class="service-red bold" font-size="17">MATTRESSES</tspan><tspan class="service-blue bold" font-size="24">AND</tspan></text>
      <text class="service-blue bold" x="1288" y="244" text-anchor="end" font-size="42">BEDDING</text>
    </g>

  </svg>
</main>
</body>
</html>
```